Animal Eye Clinic needs a Business card

We are a new veterinary ophthalmology practice (Tessaly Animal Eye Care) and we need a business card designed. We only see animal eyes - we are not a regular veterinary clinic. We already have a logo. We are looking for a professional, good looking business card to hand out to our clients. We are looking for something simple but professional and contemporary. Our logo is likely the only picture/graphic that needs to be on the card.
Updates

Contact Information for Business Card

Marisol Dunkley, BSc, DVM, MSc, DipACVO
Veterinary Ophthalmologist

Phone: 250.418.3097
Email: tessalyanimaleyecare@mailbrook.net
Website: tessalyanimaleyecare.net
Address: 1840 Pellworth Rd
Kelowna, BC, V4T 8M3

Colors

Designer to choose colors to be used in the design.

Requirements
Must have
• Our logo (attached)

```html
<!DOCTYPE html>
<html lang="en">
<head>
<meta charset="utf-8">
<title>Tessaly Animal Eye Care – Business Card</title>
<link href="https://fonts.googleapis.com/css2?family=Open+Sans:wght@400;600;700&display=swap" rel="stylesheet">
<style>
  :root {
    --teal: #0797a8;
    --grey: #6e6e6e;
    --ink: #2a2a2a;
    --muted: #6b6b6b;
    --paper: #ffffff;
    --stage: #f4f4f4;
    --edge: #d6d6d6;
  }
  * { margin: 0; padding: 0; box-sizing: border-box; }
  html, body { width: 1200px; height: 1200px; overflow: hidden; }
  body {
    background: var(--stage);
    font-family: "Open Sans", Arial, sans-serif;
    position: relative;
  }
  .card {
    position: absolute;
    left: 356px;
    width: 473px;
    height: 269px;
    overflow: hidden;
  }
  .card--front { top: 152px; background: var(--paper); border: 1px solid var(--edge); }
  .card--back { top: 746px; background: var(--teal); color: var(--paper); }

  .brand {
    position: absolute;
    left: 20px;
    top: 112px;
    display: flex;
    align-items: center;
    gap: 7px;
  }
  .brand__dot {
    width: 26px; height: 26px;
    border-radius: 50%;
    background: currentColor;
    flex: none;
  }
  .brand__name {
    font-weight: 700;
    font-size: 11px;
    line-height: 1.15;
    letter-spacing: 0.02em;
    text-transform: uppercase;
  }
  .card--front .brand { color: var(--teal); }
  .card--back .brand { color: var(--paper); }

  .mark-area {
    position: absolute;
    left: 194px;
    top: 0;
    width: 279px;
    height: 269px;
    border-radius: 140px 0 0 140px;
  }
  .card--front .mark-area { background: linear-gradient(90deg, rgba(110,110,110,0.08), rgba(110,110,110,0.55)); }
  .card--back .mark-area { background: linear-gradient(90deg, rgba(255,255,255,0.1), rgba(255,255,255,0.6)); }

  .person {
    position: absolute;
    left: 72px;
    top: 230px;
  }
  .person__name { font-size: 10.5px; color: var(--ink); line-height: 1.3; }
  .person__title { font-size: 10px; color: var(--muted); line-height: 1.3; }

  .contact {
    position: absolute;
    left: 62px;
    top: 196px;
    list-style: none;
    font-size: 9.5px;
    line-height: 15px;
  }
  .contact li { display: flex; align-items: center; gap: 6px; }
  .contact svg { width: 9px; height: 9px; fill: var(--paper); flex: none; }
</style>
</head>
<body>

  <section class="card card--front" aria-label="Business card front">
    <div class="brand">
      <span class="brand__dot"></span>
      <span class="brand__name">Tessaly<br>Animal Eye Care</span>
    </div>
    <div class="mark-area" role="img" aria-label="Large clinic brand mark: eye outline framing horse, dog and cat silhouettes"></div>
    <div class="person">
      <p class="person__name">Marisol Dunkley, BSc, DVM, MSc, DipACVO</p>
      <p class="person__title">Veterinary Ophthalmologist</p>
    </div>
  </section>

  <section class="card card--back" aria-label="Business card back">
    <div class="brand">
      <span class="brand__dot"></span>
      <span class="brand__name">Tessaly<br>Animal Eye Care</span>
    </div>
    <div class="mark-area" role="img" aria-label="Large clinic brand mark: eye outline framing horse, dog and cat silhouettes"></div>
    <ul class="contact">
      <li><svg viewBox="0 0 10 10" aria-hidden="true"><path d="M2 0.5h2l0.8 2.4-1.3 0.9a6 6 0 0 0 2.7 2.7l0.9-1.3 2.4 0.8v2a1 1 0 0 1-1 1A8.5 8.5 0 0 1 1 1.5a1 1 0 0 1 1-1z"/></svg>250.418.3097</li>
      <li><svg viewBox="0 0 10 10" aria-hidden="true"><path d="M0.5 2h9v6h-9z M0.5 2l4.5 3.5 4.5-3.5" stroke="#0797a8" stroke-width="0.6"/></svg>tessalyanimaleyecare@mailbrook.net</li>
      <li><svg viewBox="0 0 10 10" aria-hidden="true"><circle cx="5" cy="5" r="4.5"/><path d="M0.5 5h9M5 0.5v9M5 0.5c-2.5 2.5-2.5 6.5 0 9M5 0.5c2.5 2.5 2.5 6.5 0 9" stroke="#0797a8" stroke-width="0.6" fill="none"/></svg>tessalyanimaleyecare.net</li>
      <li><svg viewBox="0 0 10 10" aria-hidden="true"><circle cx="5" cy="5" r="4.5"/><path d="M5 2.2a2 2 0 0 1 2 2c0 1.5-2 3.6-2 3.6s-2-2.1-2-3.6a2 2 0 0 1 2-2z" fill="#0797a8"/></svg>1840 Pellworth Rd Kelowna, BC, V4T 8M3</li>
    </ul>
  </section>

</body>
</html>
```